Health care technology software systems

We have a solid logo. We have company colors that will need to be used as well. We just need a great business card design. We sell to health plans but want to be modern
Updates

Need extra days to review

Target Market(s)

Health technology sector selling into Health Plans

Industry/Entity Type

Health Care Technology

Contact Information for Business Card

Name, title, address, phone number, email

Requirements
Must have
• Use of Kembrata corporate colors - Uploaded w/ our logos

```html
<!DOCTYPE html>
<html lang="en">
<head>
<meta charset="utf-8">
<title>Kembrata Business Card</title>
<link href="https://fonts.googleapis.com/css2?family=Lato:wght@400;700&family=Mulish:wght@300&display=swap" rel="stylesheet">
<style>
  :root {
    --backdrop: #2a2a2a;
    --card-white: #ffffff;
    --brand-blue: #3a5ab0;
    --brand-cyan: #0ea3dc;
    --brand-green: #8cc63f;
    --bar-green: #a2c33f;
    --ink: #333333;
    --pattern-dark: #2d4796;
    --pattern-mid: #3b56a3;
    --pattern-light: #6a84cc;
  }
  * { margin: 0; padding: 0; box-sizing: border-box; }
  html, body {
    width: 1200px; height: 1200px; overflow: hidden;
    background: var(--backdrop);
    font-family: "Lato", Arial, sans-serif;
  }
  .card {
    position: absolute; left: 227px; width: 748px; height: 428px;
    box-shadow: 0 12px 30px rgba(0,0,0,0.55);
    overflow: hidden;
  }
  .card-front { top: 134px; background: var(--card-white); }
  .card-back { top: 645px; }

  .wordmark {
    position: absolute; display: flex; align-items: center; gap: 16px;
    font-family: "Mulish", Arial, sans-serif; font-weight: 300;
    line-height: 1;
  }
  .wordmark-dot { width: 50px; height: 50px; border-radius: 50%; flex: none; }
  .front-wordmark { right: 52px; top: 44px; font-size: 62px; color: var(--ink); }
  .front-wordmark .wordmark-dot { background: var(--brand-blue); }

  .accent-bar {
    position: absolute; left: 0; top: 207px; width: 22px; height: 47px;
    background: var(--bar-green);
  }
  .person-name {
    position: absolute; left: 46px; top: 202px;
    font-size: 31px; font-weight: 700; color: var(--brand-cyan); letter-spacing: 0.2px;
  }
  .person-title {
    position: absolute; left: 47px; top: 236px;
    font-size: 20px; color: var(--brand-blue);
  }
  .divider {
    position: absolute; left: 48px; top: 289px; width: 651px; height: 2px;
    background: var(--brand-green);
  }
  .contact-list {
    position: absolute; left: 47px; top: 304px; list-style: none;
    font-size: 20px; color: var(--ink);
  }
  .contact-list li { display: flex; align-items: center; gap: 8px; height: 30px; }
  .contact-list svg { width: 17px; height: 17px; flex: none; }
  .address {
    position: absolute; right: 49px; top: 303px; text-align: right;
    font-size: 20px; line-height: 30px; color: var(--ink);
  }
  .footer-band {
    position: absolute; left: 0; bottom: 0; width: 100%; height: 14px;
    background: var(--brand-blue);
  }

  .back-pattern {
    position: absolute; inset: 0;
    background: linear-gradient(100deg, var(--pattern-dark) 0%, var(--pattern-mid) 50%, var(--pattern-light) 100%);
  }
  .back-wordmark { left: 357px; top: 262px; font-size: 64px; color: var(--card-white); }
  .back-wordmark .wordmark-dot { width: 58px; height: 58px; background: var(--card-white); }
</style>
</head>
<body>
  <section class="card card-front">
    <div class="wordmark front-wordmark"><span class="wordmark-dot"></span><span>kembrata</span></div>
    <div class="accent-bar"></div>
    <h1 class="person-name">DANIEL REYES</h1>
    <p class="person-title">President</p>
    <div class="divider"></div>
    <ul class="contact-list">
      <li>
        <svg viewBox="0 0 24 24" aria-hidden="true"><path fill="#0ea3dc" d="M6.6 10.8a15.1 15.1 0 0 0 6.6 6.6l2.2-2.2c.3-.3.7-.4 1-.2 1.1.4 2.3.6 3.6.6.6 0 1 .4 1 1V20c0 .6-.4 1-1 1A17 17 0 0 1 3 4c0-.6.4-1 1-1h3.5c.6 0 1 .4 1 1 0 1.3.2 2.5.6 3.6.1.3 0 .7-.2 1z"/></svg>
        +2 418 730 2194
      </li>
      <li>
        <svg viewBox="0 0 24 24" aria-hidden="true"><rect x="2" y="5" width="20" height="14" fill="#0ea3dc"/><path d="M2 5l10 8 10-8" fill="none" stroke="#fff" stroke-width="1.6"/></svg>
        hello@kembrata.com
      </li>
      <li>
        <svg viewBox="0 0 24 24" aria-hidden="true"><circle cx="12" cy="12" r="10" fill="#0ea3dc"/><path d="M2 12h20M12 2c3 3 3 17 0 20M12 2c-3 3-3 17 0 20" fill="none" stroke="#fff" stroke-width="1.3"/></svg>
        www.kembrata.com
      </li>
    </ul>
    <address class="address" style="font-style:normal">3180 N. Harbor Avenue<br>Suite 420 Lindale, CA 92114</address>
    <div class="footer-band"></div>
  </section>

  <section class="card card-back">
    <div class="back-pattern" role="img" aria-label="Repeating brand motif pattern on blue background"></div>
    <div class="wordmark back-wordmark"><span class="wordmark-dot"></span><span>kembrata</span></div>
  </section>
</body>
</html>
```